design a construction company business card

Design business card around our logo. Card must have all the typical info: name, title, address, phone, email, business name, etc. Somewhere on the card I would like to see our motto "Built on integrity... Inspired by commitment." Consider adding a splash of bright orange to the card to complement the blues and silvers/grays in the logo. We are open to metallic inks, textures, etc. We would like to see options on both light and dark backgrounds. The font in the logo is Euro Technic Extended Regular.

```html
<!DOCTYPE html>
<html lang="en">
<head>
<meta charset="UTF-8">
<title>Marlow Contracting – Business Card</title>
<link href="https://fonts.googleapis.com/css2?family=Montserrat:wght@300;600;700&family=Open+Sans:wght@400;600&display=swap" rel="stylesheet">
<style>
  :root{
    --backdrop:#1d1d1f;
    --card:#222224;
    --card-edge:#2b2b2e;
    --brand-blue:#2f6fd6;
    --line-blue:#2a6ee0;
    --silver:#a9abb0;
    --muted:#6d6e73;
    --white:#f2f2f2;
  }
  *{margin:0;padding:0;box-sizing:border-box}
  html,body{width:1200px;height:900px;overflow:hidden;background:var(--backdrop)}
  .stage{position:relative;width:1200px;height:900px}
  .card{
    position:absolute;left:250px;width:700px;height:400px;
    background:var(--card);border:1px solid var(--card-edge);
    box-shadow:0 14px 30px rgba(0,0,0,.55);overflow:hidden;
  }
  .card--front{top:40px}
  .card--back{top:460px}

  .wordmark{
    font-family:"Montserrat",sans-serif;font-weight:700;
    color:var(--brand-blue);letter-spacing:.04em;text-transform:uppercase;
    display:flex;align-items:center;gap:14px;line-height:1.15;
  }
  .wordmark__text{display:block;white-space:nowrap}
  .wordmark__square{width:16px;height:16px;background:var(--brand-blue);flex:none}

  .card--front .wordmark{position:absolute;left:330px;top:108px;font-size:26px}
  .motto{
    position:absolute;left:330px;top:196px;
    font-family:"Open Sans",sans-serif;font-size:16px;color:var(--muted);white-space:nowrap;
  }

  .divider{position:absolute;left:0;top:120px;width:395px;height:1px;background:var(--line-blue)}
  .holder{position:absolute;left:70px;top:200px}
  .holder__name{font-family:"Montserrat",sans-serif;font-weight:300;font-size:30px;color:var(--muted);letter-spacing:.02em}
  .holder__title{font-family:"Montserrat",sans-serif;font-weight:700;font-size:16px;color:var(--brand-blue);letter-spacing:.04em;margin-top:4px}

  .card--back .wordmark{position:absolute;left:420px;top:98px;font-size:17px}
  .contacts{position:absolute;left:420px;top:190px;list-style:none;font-family:"Open Sans",sans-serif;font-size:18px;color:var(--white)}
  .contacts li{display:flex;align-items:center;gap:12px;height:32px}
  .contacts svg{width:16px;height:16px;fill:var(--brand-blue);flex:none}
</style>
</head>
<body>
<main class="stage">
  <section class="card card--front">
    <div class="wordmark">
      <span class="wordmark__square"></span>
      <span><span class="wordmark__text">Marlow</span><span class="wordmark__text">Contracting, Inc.</span></span>
    </div>
    <p class="motto">Built on integrity... Inspired by commitment</p>
  </section>

  <section class="card card--back">
    <div class="divider"></div>
    <div class="holder">
      <p class="holder__name">YOUR NAME</p>
      <p class="holder__title">JOB TITLE</p>
    </div>
    <div class="wordmark">
      <span><span class="wordmark__text">Marlow</span><span class="wordmark__text">Contracting, Inc.</span></span>
    </div>
    <ul class="contacts">
      <li><svg viewBox="0 0 16 16" aria-hidden="true"><path d="M2 5c0-2 2-3 6-3s6 1 6 3v1h-3V5H5v1H2zM3 8h10l1 6H2z"/></svg>000 000 0000</li>
      <li><svg viewBox="0 0 16 16" aria-hidden="true"><path d="M1 3h14v10H1zM2.5 4.5 8 9l5.5-4.5v-.2H2.5z"/></svg>youremail@xyz.com</li>
      <li><svg viewBox="0 0 16 16" aria-hidden="true"><path d="M8 1a5 5 0 0 1 5 5c0 4-5 9-5 9S3 10 3 6a5 5 0 0 1 5-5zm0 3a2 2 0 1 0 0 4 2 2 0 0 0 0-4z"/></svg>your address here</li>
    </ul>
  </section>
</main>
</body>
</html>
```